Letterhead and Business card for Construction company

We need a letterhead and business card with our new company logo. We are based in NY. We develop and build properties.

The design should incorporate some unique feature from the logo (shape, font...). it should look like an extension from it.

Design should be clean and elegant, professional, not too busy.

The letterhead should include:
Logo (attached)
Address
Phone
Email

Please find the attached logo images and AI file.

Target Market(s)

Construction industry professionals

Industry/Entity Type

Construction, Development

Font styles to use
Sans Serif

Colors

Designer to choose colors to be used in the design.

Requirements
Must have
• Design should incorporate logo elements, additional assets are welcome. I'd like to see some other shapes / images invorporated too.

```html
<!DOCTYPE html>
<html lang="en">
<head>
<meta charset="utf-8">
<title>Keystel Contracting — Business Card</title>
<link href="https://fonts.googleapis.com/css2?family=Montserrat:wght@400;600;700;800&display=swap" rel="stylesheet">
<style>
  :root {
    --bg: #e8e8e6;
    --card-white: #ffffff;
    --card-black: #262626;
    --motif-dark: #1c1c1c;
    --motif-light: #6e6e6e;
    --ink: #1f1f1f;
    --ink-soft: #5a5a5a;
    --accent: #f28a1d;
    --on-dark: #f4f4f4;
  }
  * { margin: 0; padding: 0; box-sizing: border-box; }
  html, body {
    width: 1200px; height: 900px; overflow: hidden;
    background: var(--bg);
    font-family: "Montserrat", sans-serif;
  }
  .stage {
    width: 1200px; height: 900px;
    display: flex; align-items: center; justify-content: center; gap: 44px;
  }
  .card {
    width: 525px; height: 300px; position: relative; overflow: hidden;
    box-shadow: 0 10px 30px rgba(0,0,0,0.12);
  }
  .card--front { background: var(--card-white); color: var(--ink); }
  .card--back { background: var(--card-black); color: var(--on-dark); }

  .wordmark {
    display: flex; align-items: center; gap: 10px;
    font-weight: 800; text-transform: uppercase; letter-spacing: 1px; line-height: 1.05;
  }
  .wordmark__square { width: 14px; height: 14px; background: var(--accent); flex: none; }
  .card--front .wordmark {
    position: absolute; left: 44px; top: 36px; font-size: 22px; color: var(--ink);
  }
  .card--back .wordmark {
    position: absolute; right: 40px; bottom: 44px;
    font-size: 28px; color: var(--on-dark);
  }

  .motif {
    position: absolute; left: 0; top: 0; width: 330px; height: 300px;
    background: linear-gradient(90deg, var(--motif-dark) 0%, #333 55%, var(--motif-light) 100%);
  }

  .person { position: absolute; left: 44px; top: 150px; }
  .person__name { font-weight: 700; font-size: 14px; letter-spacing: 0.2px; text-transform: uppercase; }
  .person__title { font-size: 13px; color: var(--accent); margin-top: 4px; }

  .address {
    position: absolute; left: 300px; top: 64px; font-style: normal;
    font-size: 13px; line-height: 1.45; color: var(--ink-soft);
  }
  .contacts {
    position: absolute; left: 300px; top: 172px; list-style: none;
    font-size: 13px; line-height: 1.6; color: var(--ink-soft);
  }
  .contacts li { display: flex; align-items: center; gap: 8px; white-space: nowrap; }
  .contacts svg { width: 12px; height: 12px; flex: none; }
</style>
</head>
<body>
<main class="stage">
  <section class="card card--front" aria-label="Business card front">
    <div class="wordmark"><span class="wordmark__square"></span><span>Keystel<br>Contracting</span></div>
    <div class="person">
      <p class="person__name">Daniel R. Whitcombe, Esq.</p>
      <p class="person__title">Brand Master</p>
    </div>
    <address class="address">
      Grounded in Craft<br>
      48 Harbor Lane, Suite 4<br>
      Millbrook, MA 01920
    </address>
    <ul class="contacts">
      <li>
        <svg viewBox="0 0 12 12" aria-hidden="true"><path d="M2 1h3l1 3-1.5 1a6 6 0 0 0 2.5 2.5L8 6l3 1v3a1 1 0 0 1-1 1A9 9 0 0 1 1 2a1 1 0 0 1 1-1z" fill="none" stroke="var(--accent)" stroke-width="1.1"/></svg>
        555-310-4420
      </li>
      <li>
        <svg viewBox="0 0 12 12" aria-hidden="true"><rect x="3" y="0.8" width="6" height="10.4" rx="1" fill="none" stroke="var(--accent)" stroke-width="1.1"/><circle cx="6" cy="9.3" r="0.6" fill="var(--accent)"/></svg>
        555-867-2291
      </li>
      <li>
        <svg viewBox="0 0 12 12" aria-hidden="true"><rect x="0.8" y="2.3" width="10.4" height="7.4" fill="none" stroke="var(--accent)" stroke-width="1.1"/><path d="M1 2.6 6 6.6l5-4" fill="none" stroke="var(--accent)" stroke-width="1.1"/></svg>
        daniel@groundedcraft.com
      </li>
      <li>
        <svg viewBox="0 0 12 12" aria-hidden="true"><circle cx="6" cy="6" r="5.2" fill="none" stroke="var(--accent)" stroke-width="1.1"/><ellipse cx="6" cy="6" rx="2.2" ry="5.2" fill="none" stroke="var(--accent)" stroke-width="1"/><path d="M0.8 6h10.4" stroke="var(--accent)" stroke-width="1"/></svg>
        www.groundedcraft.com
      </li>
    </ul>
  </section>

  <section class="card card--back" aria-label="Business card back">
    <div class="motif" role="img" aria-label="Large glossy dark decorative motif derived from the company emblem"></div>
    <div class="wordmark"><span class="wordmark__square"></span><span>Keystel<br>Contracting</span></div>
  </section>
</main>
</body>
</html>
```